Book cover for The Quiet Lioness Manual to Turn into a Powerhouse at Work

Book cover design for soft cover non-fiction book.

The front cover is what is most important at this stage, I am still gathering the testimonials and book description for the back cover so a rough to be completed later for the back is great.

Title as per above. Divided up "The Quiet Lioness Manual" (to be a series) and "Turn into a Powerhouse at Work" in this book in the series

Also for the front:

Lorna Kevesh

"The most unusual business book you will read." - Gwen Talrowicz, Author of Founder Sunrise

Background info:

This work is a blending of the masculine and feminine energies, the practical business skills with a strong focus on the inner game. I am looking for the cover to have a nod to the Dominatrix and a clear message that one can be soft (kind, open hearted) and still be strong and firm in business.

Photo options are in this file https://www.filecrate-example.net/sh/qmx41tgbw8vkrle/BBEtmkqpQ2XrLm3nXoyy94J4b?dl=0

Size 6" x 9" 179 pgs

Target Market(s)

female entreprenures

Industry/Entity Type

Business

Colors

Designer to choose colors to be used in the design.

Requirements
Must have
• I would like the title to be in a font that is bold and upscale, to contrast the softness fo the image.
• Clear and readable
• Unique look that will stand out
Should not have
• overt Dominatrix images or slant. It is about the energy not the actual.

```html
<!DOCTYPE html>
<html lang="en">
<head>
<meta charset="utf-8">
<title>The Quiet Lioness Manual – Cover Wrap</title>
<link rel="stylesheet" href="https://fonts.googleapis.com/css2?family=Great+Vibes&family=Cormorant+SC:wght@500;600&family=Cormorant+Garamond:wght@500&display=swap">
<style>
  :root {
    --backdrop-dark: #8c8c8c;
    --backdrop-light: #f4f4f4;
    --steel-blue: #3f6a95;
    --dusty-blue: #7d9bb9;
    --mist: #e6e8ec;
    --mauve: #9c6a72;
    --blush: #e9d6d8;
    --spine-blue: #5a7e9f;
    --ink: #1d1a1c;
    --paper: #ffffff;
    --shadow: rgba(20, 25, 40, 0.65);
  }
  * { margin: 0; padding: 0; box-sizing: border-box; }
  html, body { width: 1200px; height: 1200px; overflow: hidden; }
  body {
    position: relative;
    background: linear-gradient(120deg, var(--backdrop-dark) 0%, var(--backdrop-light) 55%, var(--backdrop-light) 75%, var(--backdrop-dark) 100%);
  }
  .cover-wrap {
    position: absolute;
    left: 0; top: 208px;
    width: 1200px; height: 780px;
  }
  .panel { position: absolute; top: 0; height: 780px; overflow: hidden; }
  .back-cover {
    left: 0; width: 560px;
    background:
      radial-gradient(ellipse 260px 200px at 470px 80px, rgba(156,106,114,0.7), transparent 70%),
      radial-gradient(ellipse 360px 300px at 80px 120px, var(--steel-blue), transparent 75%),
      radial-gradient(ellipse 300px 260px at 200px 460px, rgba(125,155,185,0.7), transparent 75%),
      radial-gradient(ellipse 200px 200px at 520px 720px, rgba(63,106,149,0.8), transparent 75%),
      var(--mist);
  }
  .spine {
    left: 560px; width: 76px;
    background: var(--spine-blue);
  }
  .front-cover {
    left: 636px; width: 564px;
    background:
      radial-gradient(ellipse 300px 240px at 480px 740px, var(--steel-blue), transparent 80%),
      radial-gradient(ellipse 220px 260px at 170px 560px, rgba(156,106,114,0.75), transparent 75%),
      radial-gradient(ellipse 260px 200px at 250px 350px, rgba(156,106,114,0.55), transparent 75%),
      radial-gradient(ellipse 240px 200px at 60px 720px, rgba(125,155,185,0.8), transparent 75%),
      radial-gradient(ellipse 320px 260px at 440px 150px, var(--blush), transparent 80%),
      var(--mist);
  }
  .texture { position: absolute; inset: 0; }

  .tagline {
    position: absolute;
    font-family: "Cormorant SC", serif;
    font-weight: 600;
    line-height: 1;
    letter-spacing: 1px;
  }
  .back-cover .tagline { color: var(--paper); font-size: 27px; text-shadow: 1px 1px 3px var(--shadow); }
  .front-cover .tagline { color: var(--ink); font-size: 28px; text-align: center; left: 0; width: 564px; }

  .blurb {
    position: absolute;
    font-family: "Cormorant Garamond", serif;
    font-weight: 500;
    font-size: 19px;
    line-height: 1;
  }
  .blurb.light { color: var(--paper); text-shadow: 1px 1px 2px var(--shadow); }
  .blurb.dark { color: var(--ink); }

  .author {
    position: absolute;
    font-family: "Cormorant SC", serif;
    font-weight: 600;
    font-size: 29px;
    color: var(--ink);
    line-height: 1;
    letter-spacing: 1px;
  }

  .book-title, .book-subtitle { font-weight: 400; }
  .title-script {
    position: absolute;
    font-family: "Great Vibes", cursive;
    color: var(--paper);
    line-height: 1;
    white-space: nowrap;
    text-shadow: 3px 3px 3px var(--shadow);
  }

  .spine-title {
    position: absolute;
    left: 38px; top: 400px;
    transform: translate(-50%, -50%) rotate(-90deg);
    font-family: "Great Vibes", cursive;
    font-size: 60px;
    color: var(--paper);
    white-space: nowrap;
    line-height: 1;
  }
</style>
</head>
<body>
  <div class="cover-wrap">
    <section class="panel back-cover">
      <div class="texture" role="img" aria-label="Soft blue, white and mauve spray-paint watercolour texture"></div>
      <p class="tagline" style="left:44px; top:52px;">The most Unusual</p>
      <p class="tagline" style="left:150px; top:82px;">Business Book</p>
      <p class="tagline" style="left:224px; top:112px; font-size:22px;">you will read</p>
      <p class="blurb light" style="left:56px; top:180px;">Turn into a Powerhouse at Work</p>
      <p class="blurb light" style="left:80px; top:209px;">More info goes here...</p>
      <p class="blurb dark" style="left:106px; top:420px;">More texts goes here...?</p>
      <p class="author" style="left:300px; top:728px; font-size:28px;">Lorna Kevesh</p>
    </section>

    <section class="panel spine">
      <p class="spine-title">The Quiet Lioness Manual</p>
    </section>

    <section class="panel front-cover">
      <div class="texture" role="img" aria-label="Soft blush, mauve and steel blue spray-paint watercolour texture"></div>
      <p class="tagline" style="top:22px;">The most Unusual Business Book</p>
      <p class="tagline" style="top:56px;">You will Read</p>
      <p class="author" style="left:332px; top:204px;">Lorna Kevesh</p>

      <h1 class="book-title">
        <span class="title-script" style="left:56px; top:100px; font-size:112px;">The</span>
        <span class="title-script" style="left:108px; top:210px; font-size:104px;">Quiet</span>
        <span class="title-script" style="left:124px; top:316px; font-size:92px;">Lioness</span>
        <span class="title-script" style="left:270px; top:420px; font-size:92px;">Manual</span>
      </h1>
      <h2 class="book-subtitle">
        <span class="title-script" style="left:28px; top:522px; font-size:66px;">Turn into</span>
        <span class="title-script" style="left:110px; top:598px; font-size:62px;">a Powerhouse at</span>
        <span class="title-script" style="left:330px; top:676px; font-size:74px;">Work</span>
      </h2>
    </section>
  </div>
</body>
</html>
```